Label design for organic saffron, saffron and herbal syrup

We cultivate saffron, Damszen roses, flowers and herbs. We would need a recognizable outfit (label) for our products. Theoretically (and practically) we have "converted" the family coat of arms into a kind of LOGO. I would send this in the attachment. It would be nice if - in one way or another - this LOGO / coat of arms could be used (certainly with other colors). For some time we have played with the idea of changing the second part of the family name "Lindenholm" (in German .... greuth sounds similar to Kraut / herb [English]) .... eg Lindenholm's saffron syrup into the labeling.
Our products are primarily syrups, currently herbal syrup and saffron syrup. Here the first problem arises, the only bottles / caps that are actually approved for syrup filling (hot filling) are appallingly ugly (see attachment), the only possibility of "sprucing up" is to use so-called "shrink sleeves" (here we need a diameter of 31 and a length of about 40), the colors of which are also limited. Besides the syrup, we sell saffron as a spice and various herbal mixtures (see appendix current packaging saffron). Our quantities are small (syrup 200ml-330ml), saffron in the gram range.
We also need quasi the back of the labeling (this should be able to be redefined per charge) .... Batch 1 (with small quantity has eg more of herb xy than the next batch or the saffron syrup with batch xy needs more / less saffron). In addition, we are certified organic (for this reason, the reverse side would also have to contain all the requirements of organic labeling) [see attachment].
We do not really want to address a specific clientele. Maybe just people who want to taste, enjoy, mix drinks, cook .... (and - unfortunately - don't like Vasol syrup :-) and want to pay a bit more, or find our saffron or herbs better than others) .
In summary
- Strong recognition value (possibly inclusion of "coat of arms", color variable ... although I personally don't like yellow that much)
- Saffron syrup (the color of the saffron syrup is yellow / golden-yellow-light orange, in a transparent ugly bottle)
- Herbal syrup (color variable from blue / green / brown / red elements, in transparent ugly bottle)
Saffron and other herbs (very small containers, type of container not yet fixed)
Regarding a potential "style" I can unfortunately give little information. On the one hand, I am in love with minimalism, on the other hand, I find the translucent, cryptic, implied enormously attractive and sometimes even the "overloaded" colorful has its charm. I think that all in all, it just has to be coherent, and then it will be good.
Requirements
Must have
- Integration of Code of Arms, modifiable for different products

```html
<!DOCTYPE html>
<html lang="de">
<head>
<meta charset="utf-8">
<title>Lindenholm Herbal Sirup – Label</title>
<link rel="stylesheet" href="https://fonts.googleapis.com/css2?family=Libre+Baskerville:wght@400;700&family=Open+Sans:wdth,wght@75..100,600..800&display=swap">
<style>
  :root {
    --canvas: #ffffff;
    --label-brown: #5e3a16;
    --ornament-dark: #4b2c0f;
    --ornament-gold: #a9803e;
    --gold-light: #f3dc8a;
    --gold-mid: #d2ab4f;
    --gold-dark: #9c7426;
    --panel-black: #050505;
    --text-white: #ffffff;
    --logo-navy: #23215e;
    --organic-green: #c8df9f;
    --organic-edge: #3c8a3a;
    --date-box: #ffffff;
    --text-dark: #111111;
  }
  * { margin: 0; padding: 0; box-sizing: border-box; }
  html, body { width: 784px; height: 1200px; overflow: hidden; background: var(--canvas); }

  .label {
    position: absolute; left: 45px; top: 45px;
    width: 703px; height: 1109px;
    background: var(--label-brown);
    overflow: hidden;
  }
  .ornament-field {
    position: absolute; left: 0; top: 0; width: 703px; height: 353px;
    background:
      radial-gradient(circle at 12% 45%, var(--ornament-gold) 0%, transparent 38%),
      radial-gradient(circle at 88% 45%, var(--ornament-gold) 0%, transparent 38%),
      var(--ornament-dark);
  }
  .gold-band {
    position: absolute; left: 0; top: 353px; width: 703px; height: 26px;
    background: linear-gradient(180deg, var(--gold-light), var(--gold-mid) 45%, var(--gold-dark));
  }
  .shapes { position: absolute; left: 0; top: 0; width: 784px; height: 1200px; }

  .brand {
    position: absolute; left: 238px; top: 300px; width: 312px;
    text-align: center;
    font-family: "Libre Baskerville", serif; font-weight: 400;
    font-size: 40px; color: var(--logo-navy); letter-spacing: 1px;
  }
  .brand-mark {
    position: absolute; left: 364px; top: 170px; width: 60px; height: 60px;
    border-radius: 50%; background: var(--logo-navy);
  }

  .product-name {
    position: absolute; left: 238px; top: 515px; width: 312px;
    text-align: center;
    font-family: "Libre Baskerville", serif; font-weight: 400;
    font-size: 56px; line-height: 76px; color: var(--text-white);
  }

  .vertical {
    position: absolute;
    writing-mode: vertical-rl; transform: rotate(180deg);
    font-family: "Open Sans", sans-serif; font-stretch: 80%; font-weight: 700;
    color: var(--text-white);
  }
  .ingredients {
    left: 72px; top: 463px; width: 128px; height: 650px;
    font-size: 15.5px; line-height: 21px; text-align: center; letter-spacing: 0.4px;
  }
  .producer {
    left: 636px; top: 470px; width: 70px; height: 430px;
    font-size: 14.5px; line-height: 19px; text-align: left; letter-spacing: 0.3px;
  }
  .producer .note { margin-left: 18px; }

  .best-before {
    position: absolute; left: 643px; top: 920px; width: 84px; height: 187px;
    background: var(--date-box);
  }
  .best-before span {
    position: absolute; left: 6px; bottom: 10px;
    writing-mode: vertical-rl; transform: rotate(180deg);
    font-family: "Open Sans", sans-serif; font-stretch: 80%; font-weight: 700;
    font-size: 17px; color: var(--text-dark); letter-spacing: 0.5px;
  }

  .organic-badge {
    position: absolute; left: 355px; top: 937px; width: 86px; height: 153px;
    background: var(--organic-green); border: 2px solid var(--organic-edge);
  }
  .organic-badge .seal {
    position: absolute; left: 14px; top: 55px; width: 54px; height: 54px;
    background: var(--organic-edge);
  }

  .fill-volume, .dilution {
    position: absolute; top: 1085px;
    font-family: "Open Sans", sans-serif; font-stretch: 80%; font-weight: 700;
    font-size: 21px; color: var(--text-white);
  }
  .fill-volume { left: 256px; }
  .dilution { left: 465px; }
</style>
</head>
<body>
  <div class="label">
    <div class="ornament-field" role="img" aria-label="Gold filigree mandala ornament on dark brown"></div>
    <div class="gold-band"></div>
  </div>

  <svg class="shapes" viewBox="0 0 784 1200" aria-hidden="true">
    <path d="M336 45 H453 V107 A156 156 0 1 1 336 107 Z" fill="#ffffff" stroke="#d2ab4f" stroke-width="4"/>
    <path d="M238 424 H550 V695 Q550 773 472 773 H316 Q238 773 238 695 Z" fill="#050505" stroke="#d2ab4f" stroke-width="4"/>
  </svg>

  <div class="brand-mark"></div>
  <div class="brand">Lindenholm</div>

  <div class="product-name">Herbal<br>Sirup</div>

  <p class="vertical ingredients">ZUTATEN: Lorem ipsum dolor sit amet, consectetur adipiscing elit. Morbi ultricies molestie orci. Aenean purus mauris, sodales nec diam dignissim, porttitor laoreet enim. Aliquam id sollicitudin turpis. Vivamus aliquet elit sem, et ornare ex aliquam in.</p>

  <div class="vertical producer">
    <p>*aus kontrolliert biologischer Landwirtschaft</p>
    <p class="note">Expertly crafted by: Marel-Lindenholm<br>1234 Street Name, Any City, District, Country</p>
  </div>

  <div class="best-before"><span>Best Before:</span></div>

  <div class="organic-badge" role="img" aria-label="Organic certification badge"><div class="seal"></div></div>

  <div class="fill-volume">300mL</div>
  <div class="dilution">1:7</div>
</body>
</html>
```